Ravelor Global Kft. is an online recruitment marketplace connecting the employers and recruiters together. We provide an e-bussiness solution for companies and give busines opportunity for recruiters.
We have a logo design already, which should be used on the business card.
Our colours are grey and magenta, which can be seen in the logo. Black is also welcome.
The style should be dynamic, young but professional. It should be clear, visible, elegant, not too crowded, simple but exciting.
We need the following data on the BC: name, title, address, phone,fax and mobile number, email address, website.
Target Market(s)
Our target market are companies, as this is a B2B business. We also target recruiters, recruitment professionals, headhunters.We would like to be impressive and different.
Industry/Entity Type
Business
Requirements
Must have
- We would like to promote our website, www.ravelorglb.hu.
- Please, put this on the back with a quite visible letter size.The style should be dynamic, young but professional. It should be clear, visible, elegant, not too crowded, simple but exciting.
Should not have
- We do not want to see people figures.

```html
<!DOCTYPE html>
<html lang="en">
<head>
<meta charset="utf-8">
<title>Ravelor Global Kft. – Business Cards</title>
<link rel="stylesheet" href="https://fonts.googleapis.com/css2?family=Open+Sans:wght@400;700&display=swap">
<style>
  :root {
    --stage: #c9c9c9;
    --magenta: #c4176f;
    --grey: #7d6f7c;
  }
  html, body {
    margin: 0;
    width: 1200px;
    height: 3032px;
    overflow: hidden;
    background: var(--stage);
    font-family: "Open Sans", Arial, sans-serif;
  }
  .canvas { position: relative; width: 1200px; height: 3032px; }
  .card {
    position: absolute;
    display: block;
    box-shadow: 0 2px 8px rgba(0,0,0,.18);
  }
  .card--white { --card-bg: #ffffff; --shape: #f1dbe5; --shape-2: #e6e0e6; --text-muted: #6c6c6c; }
  .card--black { --card-bg: #060606; --shape: #2a2327; --shape-2: #1a171a; --text-muted: #8a8a8a; }
  .card--pink  { --card-bg: #dcb8d2; --shape: #d5a4c4; --shape-2: #d8afcb; --text-muted: #8b6e84; }

  .card .bg { fill: var(--card-bg); }
  .card .shape { fill: var(--shape); }
  .card .shape-2 { fill: var(--shape-2); }
  .card .band { fill: var(--magenta); }
  .card .brand-square { fill: var(--magenta); }
  .card .brand { fill: var(--magenta); font-weight: 700; font-size: 22px; }
  .card .brand-small { fill: var(--magenta); font-weight: 700; font-size: 9px; }
  .card .site { fill: var(--text-muted); font-size: 8.5px; letter-spacing: .3px; }
  .card .person { fill: var(--magenta); font-size: 11px; }
  .card .role { fill: var(--text-muted); font-size: 7.5px; }
  .card .divider { stroke: var(--magenta); stroke-width: .8; }
  .card .detail { fill: var(--magenta); font-size: 7.5px; }
  .card .label { fill: var(--text-muted); font-size: 6.5px; }

  .card--front-white { left: 40px;  top: 30px;   width: 1120px; height: 640px; }
  .card--back-white  { left: 40px;  top: 700px;  width: 1120px; height: 640px; }
  .card--front-black { left: 420px; top: 1380px; width: 700px;  height: 400px; }
  .card--back-black  { left: 80px;  top: 1810px; width: 700px;  height: 400px; }
  .card--front-pink  { left: 440px; top: 2250px; width: 665px;  height: 380px; }
  .card--back-pink   { left: 80px;  top: 2650px; width: 630px;  height: 360px; }
</style>
</head>
<body>
<main class="canvas">

  <!-- Front, white edition -->
  <svg class="card card--white card--front-white" viewBox="0 0 350 200" role="group" aria-label="Card front, white">
    <rect class="bg" width="350" height="200"/>
    <polygon class="shape" points="0,0 120,0 300,180 300,185 190,185 0,10"/>
    <polygon class="shape-2" points="125,0 175,0 305,130 305,175"/>
    <rect class="brand-square" x="98" y="70" width="36" height="36"/>
    <text class="brand" x="144" y="96">Ravelor Global</text>
    <text class="site" x="225" y="140">WWW.RAVELORGLB.HU</text>
    <rect class="band" x="0" y="185" width="350" height="9"/>
  </svg>

  <!-- Back, white edition -->
  <svg class="card card--white card--back-white" viewBox="0 0 350 200" role="group" aria-label="Card back, white">
    <rect class="bg" width="350" height="200"/>
    <polygon class="shape-2" points="250,0 350,0 350,185 150,185"/>
    <polygon class="shape" points="300,0 350,0 350,185 200,185"/>
    <rect class="brand-square" x="25" y="20" width="12" height="12"/>
    <text class="brand-small" x="42" y="29.5">Ravelor Global</text>
    <text class="person" x="25" y="102">JOHN DOE</text>
    <text class="role" x="25" y="118">MARKETING VP</text>
    <line class="divider" x1="118" y1="88" x2="118" y2="168"/>
    <text class="detail" x="130" y="97">123 ADDRESS ST</text>
    <text class="detail" x="130" y="107">ANYWHERE TOWN,</text>
    <text x="130" y="126"><tspan class="label">PHONE: </tspan><tspan class="detail">000-000-000</tspan></text>
    <text x="130" y="136"><tspan class="label">FAX: </tspan><tspan class="detail">000-000-000</tspan></text>
    <text x="130" y="156"><tspan class="label">EMAIL: </tspan><tspan class="detail">INFO@RAVELORGLB.HU</tspan></text>
    <text x="130" y="166"><tspan class="label">WEB: </tspan><tspan class="detail">RAVELORGLB.HU</tspan></text>
    <rect class="band" x="0" y="185" width="350" height="9"/>
  </svg>

  <!-- Front, black edition -->
  <svg class="card card--black card--front-black" viewBox="0 0 350 200" role="group" aria-label="Card front, black">
    <rect class="bg" width="350" height="200"/>
    <polygon class="shape" points="0,0 120,0 300,180 300,185 190,185 0,10"/>
    <rect class="brand-square" x="98" y="70" width="36" height="36"/>
    <text class="brand" x="144" y="96">Ravelor Global</text>
    <text class="site" x="225" y="140">WWW.RAVELORGLB.HU</text>
    <rect class="band" x="0" y="185" width="350" height="9"/>
  </svg>

  <!-- Back, black edition -->
  <svg class="card card--black card--back-black" viewBox="0 0 350 200" role="group" aria-label="Card back, black">
    <rect class="bg" width="350" height="200"/>
    <polygon class="shape" points="300,0 350,0 350,185 200,185"/>
    <rect class="brand-square" x="25" y="20" width="12" height="12"/>
    <text class="brand-small" x="42" y="29.5">Ravelor Global</text>
    <text class="person" x="25" y="102">JOHN DOE</text>
    <text class="role" x="25" y="118">MARKETING VP</text>
    <line class="divider" x1="118" y1="88" x2="118" y2="168"/>
    <text class="detail" x="130" y="97">123 ADDRESS ST</text>
    <text class="detail" x="130" y="107">ANYWHERE TOWN,</text>
    <text x="130" y="126"><tspan class="label">PHONE: </tspan><tspan class="detail">000-000-000</tspan></text>
    <text x="130" y="136"><tspan class="label">FAX: </tspan><tspan class="detail">000-000-000</tspan></text>
    <text x="130" y="156"><tspan class="label">EMAIL: </tspan><tspan class="detail">INFO@RAVELORGLB.HU</tspan></text>
    <text x="130" y="166"><tspan class="label">WEB: </tspan><tspan class="detail">RAVELORGLB.HU</tspan></text>
    <rect class="band" x="0" y="185" width="350" height="9"/>
  </svg>

  <!-- Front, pink edition -->
  <svg class="card card--pink card--front-pink" viewBox="0 0 350 200" role="group" aria-label="Card front, pink">
    <rect class="bg" width="350" height="200"/>
    <polygon class="shape" points="0,0 120,0 300,180 300,185 190,185 0,10"/>
    <rect class="brand-square" x="98" y="70" width="36" height="36"/>
    <text class="brand" x="144" y="96">Ravelor Global</text>
    <text class="site" x="225" y="140">WWW.RAVELORGLB.HU</text>
    <rect class="band" x="0" y="185" width="350" height="9"/>
  </svg>

  <!-- Back, pink edition -->
  <svg class="card card--pink card--back-pink" viewBox="0 0 350 200" role="group" aria-label="Card back, pink">
    <rect class="bg" width="350" height="200"/>
    <polygon class="shape" points="300,0 350,0 350,185 200,185"/>
    <rect class="brand-square" x="25" y="20" width="12" height="12"/>
    <text class="brand-small" x="42" y="29.5">Ravelor Global</text>
    <text class="person" x="25" y="102">JOHN DOE</text>
    <text class="role" x="25" y="118">MARKETING VP</text>
    <line class="divider" x1="118" y1="88" x2="118" y2="168"/>
    <text class="detail" x="130" y="97">123 ADDRESS ST</text>
    <text class="detail" x="130" y="107">ANYWHERE TOWN,</text>
    <text x="130" y="126"><tspan class="label">PHONE: </tspan><tspan class="detail">000-000-000</tspan></text>
    <text x="130" y="136"><tspan class="label">FAX: </tspan><tspan class="detail">000-000-000</tspan></text>
    <text x="130" y="156"><tspan class="label">EMAIL: </tspan><tspan class="detail">INFO@RAVELORGLB.HU</tspan></text>
    <text x="130" y="166"><tspan class="label">WEB: </tspan><tspan class="detail">RAVELORGLB.HU</tspan></text>
    <rect class="band" x="0" y="185" width="350" height="9"/>
  </svg>

</main>
</body>
</html>
```